Oaths and Harbors (Book cover needed)

Oaths and Harbors: Notes from Years of Civic Labor

Author: Lorena Fabbri Okonkwo

Foreword by Ambassador Tessaly R. Brunwick

Book Trim Size: 5.5 x 8.5

```html
<!DOCTYPE html>
<html lang="en">
<head>
<meta charset="utf-8">
<title>Oaths and Harbors: Notes from Years of Civic Labor</title>
<link href="https://fonts.googleapis.com/css2?family=Montserrat:wght@500;600;700;800&display=swap" rel="stylesheet">
<style>
  :root {
    --navy-deep: #1b2030;
    --navy-mid: #262b3a;
    --flag-red: #4a2a33;
    --jacket-pink: #e0155d;
    --jacket-shade: #b80d49;
    --skin-tone: #6e4230;
    --hair-tone: #1a1412;
    --white: #ffffff;
  }
  * { margin: 0; padding: 0; box-sizing: border-box; }
  html, body {
    width: 777px; height: 1200px; overflow: hidden;
    background: var(--navy-deep);
  }
  .cover {
    position: relative; width: 777px; height: 1200px; overflow: hidden;
    font-family: "Montserrat", sans-serif; color: var(--white);
  }
  .backdrop {
    position: absolute; inset: 0;
    background:
      radial-gradient(ellipse 320px 420px at 700px 500px, var(--flag-red) 0%, transparent 70%),
      radial-gradient(ellipse 260px 380px at 60px 560px, #3a3f4d 0%, transparent 70%),
      linear-gradient(180deg, var(--navy-deep) 0%, var(--navy-mid) 55%, var(--navy-deep) 100%);
  }
  .portrait {
    position: absolute; left: 0; top: 0; width: 777px; height: 1200px;
  }
  .text-layer { position: absolute; inset: 0; text-align: center; }
  .subtitle {
    position: absolute; left: 0; right: 0; top: 86px;
    font-weight: 500; font-size: 22px; line-height: 31px;
    letter-spacing: 0.42em; padding-left: 0.42em;
  }
  .title-main {
    position: absolute; left: 0; right: 0; top: 168px;
    font-weight: 800; font-size: 176px; line-height: 1; letter-spacing: -0.01em;
  }
  .title-join {
    position: absolute; left: 0; right: 0; top: 607px;
    font-weight: 800; font-size: 44px; line-height: 1;
  }
  .title-second {
    position: absolute; left: 0; right: 0; top: 675px;
    font-weight: 800; font-size: 98px; line-height: 1; letter-spacing: -0.01em;
  }
  .author {
    position: absolute; left: 0; right: 0; top: 993px;
    font-weight: 700; font-size: 36px; line-height: 1;
  }
  .foreword-label {
    position: absolute; left: 0; right: 0; top: 1044px;
    font-weight: 600; font-size: 19px; line-height: 1;
  }
  .foreword-name {
    position: absolute; left: 0; right: 0; top: 1066px;
    font-weight: 700; font-size: 31px; line-height: 35px;
  }
</style>
</head>
<body>
<main class="cover">
  <div class="backdrop" role="img" aria-label="Dark navy backdrop with a softly blurred flag"></div>

  <svg class="portrait" viewBox="0 0 777 1200" role="img" aria-label="Portrait photograph of the author in a pink blazer, smiling, hands clasped">
    <defs>
      <linearGradient id="figure-tone" x1="0" y1="0" x2="0" y2="1">
        <stop offset="0" stop-color="var(--hair-tone)"/>
        <stop offset="0.12" stop-color="var(--skin-tone)"/>
        <stop offset="0.3" stop-color="var(--skin-tone)"/>
        <stop offset="0.36" stop-color="var(--jacket-pink)"/>
        <stop offset="1" stop-color="var(--jacket-shade)"/>
      </linearGradient>
    </defs>
    <path d="M388 272 C 330 272 262 300 262 390 C 262 460 290 520 318 545
             L 318 575 C 250 600 130 640 75 680 C 40 720 30 820 26 1200
             L 752 1200 C 748 820 738 720 705 680 C 650 640 528 600 460 575
             L 460 545 C 490 520 514 460 514 390 C 514 300 446 272 388 272 Z"
          fill="url(#figure-tone)"/>
  </svg>

  <div class="text-layer">
    <p class="subtitle">NOTES FROM<br>YEARS OF CIVIC LABOR</p>
    <h1 class="title-main">OATHS</h1>
    <p class="title-join">AND</p>
    <p class="title-second">HARBORS</p>
    <p class="author">LORENA FABBRI OKONKWO</p>
    <p class="foreword-label">FOREWORD BY</p>
    <p class="foreword-name">AMBASSADOR<br>TESSALY R. BRUNWICK</p>
  </div>
</main>
</body>
</html>
```